Coldbrook IT
Business Cards & Stationary
Hi everyone,
Thanks a lot for your efforts so far. Just a few pointers.
If possible leave a little white space somewhere on the business card incase someone wants to write on it. I write on business cards all the time.
I do prefer the dark background/light symbol. Also please try to incorporate the designed website address.
Thanks for your efforts so far and keep them coming!
Hi,
Please can you also provide samples of letterheaded paper and compliment slips as I would like the same theme carried through.
Thanks and keep up the good work!
Can you also try the dark background with the lighter symbol for the front of the business card.

```html
<!DOCTYPE html>
<html lang="en">
<head>
<meta charset="utf-8">
<title>Coldbrook IT – Business Card</title>
<link href="https://fonts.googleapis.com/css2?family=Open+Sans:wght@400;600&display=swap" rel="stylesheet">
<style>
  :root {
    --backdrop: #d9d6d1;
    --card-black: #050505;
    --card-dark: #1a1a1a;
    --card-mid: #3a3a3a;
    --silver-light: #f2f2f2;
    --silver-mid: #c9c9c9;
    --silver-dark: #9a9a9a;
    --text-light: #e8e8e8;
    --text-grey: #a8a8a8;
    --text-dark: #111111;
  }
  * { margin: 0; padding: 0; box-sizing: border-box; }
  html, body { width: 1200px; height: 929px; overflow: hidden; }
  body {
    background: var(--backdrop);
    font-family: "Open Sans", Arial, sans-serif;
    position: relative;
  }
  .card {
    position: absolute;
    overflow: hidden;
    box-shadow: 0 6px 18px rgba(0,0,0,0.35);
  }

  /* Contact side */
  .card-contact {
    left: 477px; top: 55px;
    width: 608px; height: 369px;
    background: var(--card-black);
  }
  .contact-details {
    position: absolute;
    left: 0; right: 0; top: 30px;
    text-align: center;
    color: var(--text-light);
    font-size: 13px;
    line-height: 20px;
  }
  .contact-details .address { margin-bottom: 18px; }
  .brand-name {
    font-weight: 600;
    color: var(--text-light);
    letter-spacing: 2px;
    text-transform: uppercase;
  }
  .card-contact .brand {
    position: absolute;
    left: 0; right: 0; top: 160px;
    text-align: center;
  }
  .card-contact .brand-name { font-size: 26px; }
  .card-contact .brand-tagline {
    font-size: 7px; letter-spacing: 2px; color: var(--text-grey);
    margin-top: 2px;
  }
  .silver-band {
    position: absolute; left: 0; top: 0;
    width: 608px; height: 369px;
  }
  .holder {
    position: absolute; left: 0; right: 0; top: 290px;
    text-align: center; color: var(--text-dark);
  }
  .holder-name { font-size: 24px; line-height: 32px; }
  .holder-role { font-size: 20px; line-height: 28px; }

  /* Brand side */
  .card-brand {
    left: 351px; top: 437px;
    width: 598px; height: 412px;
    background: radial-gradient(ellipse at 50% 42%, var(--card-mid) 0%, var(--card-dark) 45%, var(--card-black) 100%);
  }
  .card-brand .brand {
    position: absolute; left: 0; right: 0; top: 130px;
    text-align: center;
  }
  .card-brand .brand-name { font-size: 34px; }
  .card-brand .brand-tagline {
    margin-top: 40px;
    font-size: 12px; letter-spacing: 1.5px;
    color: var(--text-grey); text-transform: uppercase;
  }
  .card-brand .brand-web {
    margin-top: 2px;
    font-size: 13px; letter-spacing: 1px; color: var(--text-light);
  }
</style>
</head>
<body>

<section class="card card-contact">
  <svg class="silver-band" viewBox="0 0 608 369" aria-hidden="true">
    <defs>
      <linearGradient id="silver" x1="0" y1="0" x2="1" y2="0">
        <stop offset="0" stop-color="var(--silver-dark)"/>
        <stop offset="0.5" stop-color="var(--silver-light)"/>
        <stop offset="1" stop-color="var(--silver-dark)"/>
      </linearGradient>
      <linearGradient id="silver-edge" x1="0" y1="0" x2="1" y2="0">
        <stop offset="0" stop-color="#666"/>
        <stop offset="0.5" stop-color="#ffffff"/>
        <stop offset="1" stop-color="#666"/>
      </linearGradient>
    </defs>
    <path d="M0 232 L304 268 L608 232 L608 369 L0 369 Z" fill="url(#silver-edge)"/>
    <path d="M0 240 L304 276 L608 240 L608 369 L0 369 Z" fill="url(#silver)"/>
  </svg>
  <div class="contact-details">
    <p class="address">18 Harrow Quay<br>Fennick Bridge, Dublin 9</p>
    <p>Cell : +353 (0) 861204738 &nbsp;|&nbsp; Email : niall@coldbrookit.com</p>
    <p>Web : www.coldbrookit.com</p>
  </div>
  <div class="brand">
    <p class="brand-name">Coldbrook IT</p>
    <p class="brand-tagline">CREATIVE SOFTWARE SOLUTIONS</p>
  </div>
  <div class="holder">
    <p class="holder-name">Niall Dorrance</p>
    <p class="holder-role">Director</p>
  </div>
</section>

<section class="card card-brand">
  <div class="brand">
    <p class="brand-name">Coldbrook IT</p>
    <p class="brand-tagline">Creative Software Solutions</p>
    <p class="brand-web">www.coldbrookit.com</p>
  </div>
</section>

</body>
</html>
```